Photography Studio Prep Guide Design Needed

I have a prep guide I send to all parents who book a session - It is outdated and ugly. I want a gorgeous, clean, modern upscale look for the brochure I send.

I already have the text and can provide photos for the final design. I want the cover to be clean and upscale and modern, with a happy feel.

Target Market(s)

My clients for an upscale Newborn Photography Studio

Requirements
Must have
• space for my photos, an upscale clean feel
Nice to have
• I love color, but don't want the brochure to look busy. I love cream, white, pale pink.

```html
<!DOCTYPE html>
<html lang="en">
<head>
<meta charset="utf-8">
<title>Newborn Session Prep Guide</title>
<link rel="stylesheet" href="https://fonts.googleapis.com/css2?family=Libre+Baskerville&family=Dancing+Script:wght@500&family=Arimo:wght@400;700&display=swap">
<style>
  :root {
    --backdrop: #ededed;
    --paper: #ffffff;
    --sky: #aec8e3;
    --sky-deep: #8fb0d6;
    --blush: #f6dede;
    --blush-deep: #e9bcbc;
    --rose: #d94c9a;
    --plum: #8a2552;
    --ink: #1c1c1c;
    --grey: #6e6e6e;
    --lilac: #9b63b8;
    --coral: #e7a3a8;
    --sage: #d9d3c8;
    --denim: #3f64b4;
  }
  * { box-sizing: border-box; margin: 0; padding: 0; }
  html, body { width: 1200px; height: 883px; overflow: hidden; background: var(--backdrop); }
  .spread { position: relative; width: 1200px; height: 883px; }
  .page { position: absolute; background: var(--paper); overflow: hidden; }

  /* Cover */
  .cover { left: 38px; top: 28px; width: 547px; height: 818px; }
  .cover-photo { position: absolute; left: 0; top: 0; width: 547px; height: 410px;
    background: linear-gradient(160deg, var(--sky) 0%, #c5d8ec 55%, var(--sky-deep) 100%); }
  .scallop { position: absolute; left: 0; top: 378px; width: 547px; height: 40px; }
  .brand-panel { position: absolute; left: 50px; top: 0; width: 248px; height: 164px;
    background: #dfe9f5; display: flex; flex-direction: column; align-items: center; justify-content: center; gap: 4px; }
  .brand-name { font-family: "Libre Baskerville", serif; font-size: 17px; color: var(--grey); letter-spacing: 0.2px; text-align: center; line-height: 1.4; }
  .brand-mark { width: 10px; height: 10px; border-radius: 50%; background: var(--blush-deep); margin-bottom: 6px; }
  .cover-title { position: absolute; left: 0; width: 547px; top: 402px; text-align: center; }
  .cover-title .kicker { font-family: "Libre Baskerville", serif; font-size: 27px; color: var(--grey); letter-spacing: 0.5px; }
  .cover-title .script { font-family: "Dancing Script", cursive; font-size: 34px; color: var(--rose); margin-top: 0; line-height: 1.1; }
  .cover-rule { position: absolute; left: 0; top: 496px; width: 547px; height: 4px; background: var(--blush); }
  .gallery { position: absolute; left: 0; top: 500px; width: 547px; height: 318px; }
  .gallery-tile { position: absolute; top: 0; height: 318px; }
  .tile-a { left: 0; width: 178px; background: linear-gradient(160deg, #c59ad8, var(--lilac) 60%, #6d3b86); }
  .tile-b { left: 182px; width: 176px; background: linear-gradient(180deg, #f4e4e6, var(--coral) 75%, #d9666f); }
  .tile-c { left: 363px; width: 184px; background: linear-gradient(170deg, #e3ddd3, #f4f1ec 50%, #b8cf93); }

  /* Instructions page */
  .guide { left: 610px; top: 30px; width: 548px; height: 820px; }
  .guide-photo { position: absolute; left: 0; top: 0; width: 548px; height: 237px;
    background: linear-gradient(150deg, var(--denim) 0%, #c94b4b 45%, #3a3a3a 100%); }
  .ribbon { position: absolute; left: 20px; top: 196px; width: 510px; height: 66px; }
  .ribbon-title { position: absolute; left: 20px; top: 203px; width: 510px; text-align: center;
    font-family: "Dancing Script", cursive; font-size: 30px; color: var(--plum); }
  .intro { position: absolute; left: 20px; top: 264px; width: 510px; text-align: center;
    font-family: "Arimo", sans-serif; font-size: 12.8px; line-height: 16px; color: var(--ink); }
  .section { position: absolute; left: 38px; width: 472px; }
  .section-head { display: flex; align-items: center; gap: 18px; margin-left: 21px; height: 48px; }
  .section-icon { width: 46px; height: 46px; }
  .section-title { font-family: "Dancing Script", cursive; font-size: 28px; color: var(--plum); }
  .section-body { margin-top: 14px; font-family: "Arimo", sans-serif; font-size: 12.8px; line-height: 16.1px;
    color: var(--ink); text-align: justify; }
  .section-body p strong { font-weight: 700; }
  .nursing { top: 330px; }
  .feeding { top: 559px; }
</style>
</head>
<body>
<div class="spread">

  <section class="page cover">
    <div class="cover-photo" role="img" aria-label="Sleeping newborn in a striped knotted hat and striped trousers on a pale blue blanket"></div>
    <svg class="scallop" viewBox="0 0 547 40" preserveAspectRatio="none" aria-hidden="true">
      <path d="M0 22 Q34 6 68 22 Q102 6 136 22 Q170 6 204 22 Q238 6 273 22 Q308 6 342 22 Q376 6 410 22 Q444 6 478 22 Q512 6 547 22 L547 40 L0 40 Z" fill="var(--blush)"/>
      <path d="M0 26 Q34 10 68 26 Q102 10 136 26 Q170 10 204 26 Q238 10 273 26 Q308 10 342 26 Q376 10 410 26 Q444 10 478 26 Q512 10 547 26 L547 40 L0 40 Z" fill="var(--paper)"/>
    </svg>
    <div class="brand-panel">
      <span class="brand-mark"></span>
      <div class="brand-name">CLARA WHITMORE<br>PHOTOGRAPHY</div>
    </div>
    <div class="cover-title">
      <div class="kicker">NEWBORN SESSION</div>
      <div class="script">Prep Guide</div>
    </div>
    <div class="cover-rule"></div>
    <div class="gallery">
      <div class="gallery-tile tile-a" role="img" aria-label="Newborn in a purple bonnet wrapped on purple fur"></div>
      <div class="gallery-tile tile-b" role="img" aria-label="Twin newborns with flower headbands on a floral backdrop"></div>
      <div class="gallery-tile tile-c" role="img" aria-label="Newborn with a green flower headband wrapped in green in a white nest"></div>
    </div>
  </section>

  <section class="page guide">
    <div class="guide-photo" role="img" aria-label="Parent in a superhero shirt holding a newborn wearing glasses and a red cape"></div>
    <svg class="ribbon" viewBox="0 0 510 66" aria-hidden="true">
      <polygon points="0,8 30,8 30,58 0,58 14,33" fill="var(--blush-deep)"/>
      <polygon points="510,8 480,8 480,58 510,58 496,33" fill="var(--blush-deep)"/>
      <polygon points="20,2 490,2 480,62 30,62" fill="var(--blush)"/>
    </svg>
    <div class="ribbon-title">Parent Instructions &amp; Preparations</div>
    <div class="intro">
      Congratulations on expecting a baby!<br>
      Here are my instructions to ensure a successful newborn photography session.<br>
      Please follow these instructions as closely as possible.
    </div>

    <div class="section nursing">
      <div class="section-head">
        <svg class="section-icon" viewBox="0 0 46 46" aria-hidden="true">
          <circle cx="23" cy="23" r="22" fill="var(--blush)"/>
          <path d="M16 13 Q23 20 30 13 L31 26 Q23 36 15 26 Z" fill="var(--paper)"/>
        </svg>
        <span class="section-title">Nursing</span>
      </div>
      <div class="section-body">
        <p>If you are nursing, please avoid eating anything spicy (hot sauce, hot peppers, curry, etc.) that might upset baby’s tummy for 24 hours preceding your scheduled session.</p>
        <p>Please if you are breastfeeding do NOT drink caffeine or coffee before your session – I know this is hard but baby will be wired if you have caffeine.</p>
        <p>If you notice baby has a lot of gas after feedings please check with your pediatrician and bring gas drops (Tummease or other brand) to your session. The most common reason a baby will not settle for a session is gas pressure/discomfort.</p>
      </div>
    </div>

    <div class="section feeding">
      <div class="section-head">
        <svg class="section-icon" viewBox="0 0 46 46" aria-hidden="true">
          <circle cx="23" cy="23" r="22" fill="var(--blush)"/>
          <g transform="rotate(35 23 23)">
            <rect x="18" y="16" width="10" height="19" rx="3" fill="var(--paper)"/>
            <rect x="20" y="10" width="6" height="6" rx="2" fill="var(--paper)"/>
          </g>
        </svg>
        <span class="section-title">Feeding</span>
      </div>
      <div class="section-body">
        <p>Feed the baby as much as possible in the 24 hours preceding your session – this will help minimize the amount baby needs to feed during the session, and will help baby sleep as long and as soundly as possible. Feed baby 2-3 hours before your session and not again until you arrive. This feeding is planned in your session time and it’s not rushed.</p>
        <p><strong>Please bring an extra bottle of formula or breastmilk to the session if possible – sometimes a small amount of milk in a bottle can quickly soothe a baby back to sleep without requiring a full feeding.</strong> I will respect your wishes if you choose not to use a bottle, but please understand we may have to pass on some poses if baby will not settle in position, and I cannot use a bottle to soothe them into the pose.</p>
      </div>
    </div>
  </section>

</div>
</body>
</html>
```